Business Card Design for Oncology Consulting Company

We need a business card design using a logo that has already been created.

Company name is: ORBVA - Guild for Lumora Mapping, Welfare and Outreach

We would also like to include the following pieces of information on the business card:
Name
Title
US Address (street, city, state, zip, country)
Email address
Website address

Target Market(s)

The target customers are physicians (oncologists, pathologists) in Greece, Iran, US, etc who would refer patients to our company for a second medical opinion/genetic counseling for cancer.

Industry/Entity Type

Business

Colors

Designer to choose colors to be used in the design.

Requirements
Must have
• Must contain logo in attached file and elements described above.

```html
<!DOCTYPE html>
<html lang="en">
<head>
<meta charset="utf-8">
<title>ORBVA Business Card</title>
<link href="https://fonts.googleapis.com/css2?family=Ubuntu:wght@500;700&family=Open+Sans:wght@400;600&display=swap" rel="stylesheet">
<style>
  :root {
    --backdrop: #3a3a3c;
    --card-front: #ffffff;
    --card-back: #e6e7e8;
    --brand-blue: #1569b0;
    --band-grey: #bcbec0;
    --text-grey: #58595b;
    --tag-grey: #a7a9ac;
    --ink: #111111;
  }
  * { margin: 0; padding: 0; box-sizing: border-box; }
  html, body { width: 1200px; height: 999px; overflow: hidden; }
  body { background: var(--backdrop); position: relative; font-family: "Open Sans", sans-serif; }

  .card { position: absolute; overflow: hidden; }
  .card--front { left: 120px; top: 65px; width: 759px; height: 433px; background: var(--card-front); }
  .card--back { left: 332px; top: 526px; width: 758px; height: 433px; background: var(--card-back); }

  .brand { position: absolute; display: flex; align-items: center; }
  .brand__name { font-family: "Ubuntu", sans-serif; font-weight: 700; color: var(--brand-blue); line-height: 1; letter-spacing: 0.5px; }
  .brand__dot { border-radius: 50%; background: var(--brand-blue); }
  .brand__tagline { position: absolute; font-family: "Open Sans", sans-serif; font-weight: 600; color: var(--tag-grey); text-transform: uppercase; white-space: nowrap; }

  .card--front .brand { left: 26px; top: 46px; }
  .card--front .brand__name { font-size: 70px; }
  .card--front .brand__dot { width: 16px; height: 16px; margin-left: 22px; margin-top: 14px; }
  .card--front .brand__tagline { left: 244px; top: 98px; font-size: 7px; letter-spacing: 0.1px; }

  .card--back .brand { left: 76px; top: 172px; }
  .card--back .brand__name { font-size: 92px; }
  .card--back .brand__dot { width: 20px; height: 20px; margin-left: 28px; margin-top: 18px; }
  .card--back .brand__tagline { left: 353px; top: 238px; font-size: 9px; letter-spacing: 0.1px; }

  .holder { position: absolute; left: 31px; top: 283px; }
  .holder__name { font-family: "Ubuntu", sans-serif; font-weight: 700; font-size: 34px; color: var(--brand-blue); line-height: 1.1; }
  .holder__title { font-size: 20px; color: var(--ink); margin-top: 6px; margin-left: 2px; }

  .blurb { position: absolute; left: 480px; top: 188px; font-size: 19px; line-height: 25px; color: var(--text-grey); }

  .contacts { position: absolute; left: 482px; top: 288px; list-style: none; color: var(--text-grey); font-size: 18px; }
  .contacts__item { display: flex; align-items: center; height: 25px; }
  .contacts__icon { width: 18px; height: 16px; fill: var(--text-grey); }
  .contacts__sep { margin: 0 10px 0 24px; }

  .footer-bands { position: absolute; left: 0; bottom: 0; width: 759px; height: 57px; }
</style>
</head>
<body>
  <section class="card card--front" aria-label="Business card front">
    <div class="brand">
      <span class="brand__name">ORBVA</span>
      <span class="brand__dot"></span>
      <span class="brand__tagline">Guild for Lumora Mapping, Welfare and Outreach</span>
    </div>

    <p class="blurb">Lorem ipsum dolor sit amet,<br>consectetur adipiscing elit.<br>Donec accumsan.</p>

    <div class="holder">
      <h1 class="holder__name">Person Name</h1>
      <p class="holder__title">designation</p>
    </div>

    <ul class="contacts">
      <li class="contacts__item">
        <svg class="contacts__icon" viewBox="0 0 18 16" aria-hidden="true"><path d="M5 1c1 0 1.5 2 1.8 3 .2.8-1 1.2-1 2 0 1.5 1.5 4 3 5 .7.4 1.2-.7 2-.5 1 .3 2.5 1.2 2.5 2 0 1-1.5 2.5-3 2.5C6 15 2 9.5 2 5c0-2 1.5-4 3-4z"/></svg>
        <span class="contacts__sep">:</span><span>555 0142 7788</span>
      </li>
      <li class="contacts__item">
        <svg class="contacts__icon" viewBox="0 0 18 16" aria-hidden="true"><path d="M1 3h16v11H1z M2.5 4.5 9 9.5l6.5-5" fill="none" stroke="#58595b" stroke-width="1.6"/><path d="M1 3h16L9 9z"/></svg>
        <span class="contacts__sep">:</span><span>hello@orbva-guild.org</span>
      </li>
      <li class="contacts__item">
        <svg class="contacts__icon" viewBox="0 0 18 16" aria-hidden="true"><path d="M16 1 2 7l6 1.5L9.5 15z"/></svg>
        <span class="contacts__sep">:</span><span>www.orbva-guild.org</span>
      </li>
    </ul>

    <svg class="footer-bands" viewBox="0 0 759 57" aria-hidden="true">
      <rect x="0" y="0" width="759" height="57" fill="var(--band-grey)"/>
      <polygon points="0,6 572,6 592,57 0,57" fill="var(--card-front)"/>
      <polygon points="0,12 568,12 585,57 0,57" fill="var(--brand-blue)"/>
    </svg>
  </section>

  <section class="card card--back" aria-label="Business card back">
    <div class="brand">
      <span class="brand__name">ORBVA</span>
      <span class="brand__dot"></span>
      <span class="brand__tagline">Guild for Lumora Mapping, Welfare and Outreach</span>
    </div>
  </section>
</body>
</html>
```